Work Van

Side of the Van:
[Logo]
• Size: Large and centered on the front door area.
• Color: Use brand colors.
[Tall Pine General Construction Inc]
• Font: Bold, easy-to-read
• Placement: Directly beneath or next to the logo. (as recommended)
[Tagline]
• "I can do all things through Christ who strengthens me" Philippians 4:13 (beneath the logo in smaller font size)
• Text: “Your Dreams, Our Commitment: Reliable Construction, Insured and WSRB Certified!”
• Font: Slightly smaller than the company name. (where you recommend)
[Services Offered]
• Icons/Illustrations:
o “Residential and Commercial Construction” - icon of a hammer.
o “Remodeling Services” Icon of a house and paintbrush.
o “Structural Framing Services” Icon of structural skeleton of house -.
• Placement: Horizontal alignment beneath the company name and tagline, with icons in a row.
[Contact Information]
• Phone Number: “Call Us: 508-374-2915”
• Website: “tpgcinc.example”
• Email: tpgcsince2004@mailbox.example
• Instagram QR code (attached on file)
• Font: Clear and bold, positioned either below the services offered or at the rear of the van.
Rear of the Van:
[Logo]
• Size: Medium, near the top or center.
[Company Name and Contact Information]
• "Tall Pine General Construction Inc."
• "Call Us: 508-374-2915"
• “www.tpgcinc.example”
• Font: Large enough to be readable from a distance.
Color and Background:
• Background Color: A solid color that complements your brand (e.g., light blue or white).
• Graphics: Consider a subtle pattern or textured background (e.g., a gradient or images of tools) that doesn't overwhelm the main information.
Example Visualization:
• The logo at the top left.
• A bold company name next to it.
• A tagline underneath.
• Icons and short descriptors for services spread out underneath or along the side.
• Contact info sourced at the bottom or along the rear.

```html
<!DOCTYPE html>
<html lang="en">
<head>
<meta charset="utf-8">
<title>Tall Pine General Construction Inc – Work Van Wrap</title>
<link rel="stylesheet" href="https://fonts.googleapis.com/css2?family=Teko:wght@500;600&family=Open+Sans:wght@400;600&display=swap">
<style>
  :root{
    --red:#e3141c;
    --blue:#1d1a9e;
    --white:#f5f5f5;
    --ink:#161616;
    --skirt:#2b2b2d;
    --glass:#2c3038;
    --gold:#d49a36;
    --page:#ffffff;
  }
  *{margin:0;padding:0;box-sizing:border-box}
  html,body{width:885px;height:1200px;overflow:hidden;background:var(--page)}
  .canvas{position:relative;width:885px;height:1200px;font-family:"Teko",sans-serif}
  .wrap-shapes{position:absolute;left:0;top:0}
  .abs{position:absolute}

  .company-name{font-weight:600;color:#fff;font-size:33px;line-height:.92;letter-spacing:.3px;white-space:nowrap}
  .company-name .w-red{color:var(--red)}
  .company-name .w-boxed{color:var(--blue);background:#fff;padding:0 3px;margin:0 2px}
  .tagline{font-weight:500;color:#fff;font-size:12.5px;line-height:1.05;text-transform:uppercase;white-space:nowrap}
  .tagline span{display:inline-block;background:var(--ink);padding:0 4px}

  .services{list-style:none;color:var(--red);font-weight:500;font-size:13.5px;line-height:15.5px;text-transform:uppercase;white-space:nowrap}
  .services li{display:flex;align-items:center;gap:5px}
  .services li span{background:#fff;padding:0 3px;line-height:13px}
  .services svg{width:13px;height:13px;flex:none}

  .contact{white-space:nowrap}
  .contact .row{display:flex;align-items:center;gap:5px}
  .contact .phone{color:var(--red);font-weight:600;font-size:30px;line-height:28px;letter-spacing:.5px}
  .contact .email{color:var(--blue);font-weight:600;font-size:10.5px;line-height:14px;letter-spacing:.4px;text-transform:uppercase}
  .contact .dot{width:15px;height:15px;border-radius:50%;flex:none;display:flex;align-items:center;justify-content:center}
  .contact .dot.blue{background:var(--blue)}
  .contact .dot.red{background:var(--red)}
  .contact .dot svg{width:9px;height:9px}

  .website{color:var(--gold);font-weight:500;font-size:12.5px;text-transform:uppercase;letter-spacing:.4px}

  .logo-lockup{display:flex;align-items:center;justify-content:space-between}
  .worker{flex:none;background:#1b1b1b}
  .worker.light{background:#e4e6f2}
  .brand{display:flex;align-items:center;gap:4px}
  .brand-square{background:var(--red);flex:none}
  .brand-name{font-weight:600;color:var(--blue);white-space:nowrap;line-height:1}
  .brand-sub{font-family:"Open Sans",sans-serif;font-weight:400;color:#333;white-space:nowrap;text-align:center}

  .front-contact{color:#fff;font-weight:500;font-size:11px;letter-spacing:.4px;text-transform:uppercase;white-space:nowrap}
</style>
</head>
<body>
<div class="canvas">

  <svg class="wrap-shapes" width="885" height="1200" viewBox="0 0 885 1200" xmlns="http://www.w3.org/2000/svg">
    <defs>
      <clipPath id="side-body">
        <path d="M118,270 L120,215 Q125,195 150,190 L230,170 L320,62 Q330,52 350,52 L812,52 Q824,54 826,70 L832,290 L832,312 L118,312 Z"/>
      </clipPath>
      <g id="side-panel">
        <g clip-path="url(#side-body)">
          <rect x="90" y="40" width="760" height="290" fill="var(--blue)"/>
          <polygon points="90,40 469,40 141,320 90,320" fill="var(--red)"/>
          <polygon points="469,40 500,40 674,320 141,320" fill="var(--white)"/>
          <rect x="90" y="258" width="760" height="60" fill="var(--skirt)"/>
          <rect x="90" y="288" width="760" height="8" fill="var(--white)"/>
          <path d="M240,190 L300,118 Q310,108 330,108 L378,108 L378,198 Z" fill="var(--glass)"/>
          <rect x="392" y="108" width="1" height="202" fill="#bbb"/>
          <rect x="812" y="180" width="14" height="78" rx="3" fill="var(--red)"/>
        </g>
        <circle cx="237" cy="312" r="46" fill="var(--page)"/>
        <circle cx="692" cy="312" r="46" fill="var(--page)"/>
      </g>
    </defs>

    <use href="#side-panel"/>
    <use href="#side-panel" transform="translate(886,315) scale(-1,1)"/>

    <rect x="85" y="705" width="330" height="300" rx="22" fill="var(--red)"/>
    <rect x="98" y="768" width="304" height="112" rx="10" fill="var(--glass)"/>
    <polygon points="133,890 350,890 318,944 170,944" fill="var(--white)"/>
    <rect x="90" y="1000" width="320" height="130" rx="14" fill="var(--skirt)"/>
    <rect x="27" y="848" width="34" height="64" rx="7" fill="var(--skirt)"/>
    <rect x="426" y="848" width="34" height="64" rx="7" fill="var(--skirt)"/>

    <rect x="498" y="705" width="333" height="300" rx="20" fill="var(--blue)"/>
    <rect x="664" y="712" width="1" height="180" fill="#3a36b5"/>
    <rect x="489" y="892" width="16" height="108" rx="4" fill="var(--red)"/>
    <rect x="824" y="892" width="16" height="108" rx="4" fill="var(--red)"/>
    <rect x="492" y="1000" width="346" height="130" rx="12" fill="var(--skirt)"/>
  </svg>

  <!-- Side A (front left) -->
  <div class="abs logo-lockup" style="left:396px;top:104px;width:188px;height:60px">
    <div class="worker" role="img" aria-label="Worker silhouette pushing up a wall frame" style="width:32px;height:58px;border-radius:12px 12px 3px 3px"></div>
    <div class="brand"><div class="brand-square" style="width:11px;height:11px"></div><div class="brand-name" style="font-size:24px">TALL PINE</div></div>
    <div class="worker" role="img" aria-label="Worker silhouette pushing up a wall frame" style="width:32px;height:58px;border-radius:12px 12px 3px 3px"></div>
  </div>
  <div class="abs brand-sub" style="left:410px;top:170px;width:160px;font-size:10px">GENERAL CONSTRUCTION INC</div>

  <div class="abs contact" style="left:398px;top:206px">
    <div class="row"><span class="dot blue"><svg viewBox="0 0 10 10"><path d="M2 1l2 2-1 1.2c.6 1.2 1.6 2.2 2.8 2.8L7 6l2 2-1.3 1.3C4.5 9 1 5.5.7 2.3Z" fill="#fff"/></svg></span><span class="phone">508-374-2915</span></div>
    <div class="row"><span class="dot red"><svg viewBox="0 0 10 10"><rect x="1" y="2.5" width="8" height="5.5" fill="none" stroke="#fff" stroke-width="1"/><path d="M1 2.5l4 3 4-3" fill="none" stroke="#fff" stroke-width="1"/></svg></span><span class="email">tpgcsince2004@mailbox.example</span></div>
  </div>

  <div class="abs company-name" style="left:588px;top:80px">
    <span class="w-red">TALL</span><span class="w-boxed">PINE</span>GENERAL<br>CONSTRUCTION INC
  </div>
  <div class="abs tagline" style="left:597px;top:147px">
    <span>I can do all things through Christ</span><br><span>who strengthens me" Philippians 4:13</span>
  </div>
  <ul class="abs services" style="left:588px;top:204px">
    <li><svg viewBox="0 0 12 12"><path d="M1 6L6 1.5 11 6V11H1Z" fill="none" stroke="#fff" stroke-width="1.3"/></svg><span>Remodeling Services</span></li>
    <li><svg viewBox="0 0 12 12"><path d="M1 6L6 1.5 11 6V11H1ZM1 8.5H11M6 4V11" fill="none" stroke="#fff" stroke-width="1.1"/></svg><span>Structural Framing Services</span></li>
    <li><svg viewBox="0 0 12 12"><path d="M2 11L7 6M5 3.5L8.5 1 11 3.5 8.5 6Z" fill="none" stroke="#fff" stroke-width="1.4"/></svg><span>Residential &amp; Commercial Construction</span></li>
  </ul>
  <div class="abs website" style="left:300px;top:246px">tpgcinc.example</div>

  <!-- Side B (front right) -->
  <div class="abs logo-lockup" style="left:312px;top:418px;width:188px;height:60px">
    <div class="worker" role="img" aria-label="Worker silhouette pushing up a wall frame" style="width:32px;height:58px;border-radius:12px 12px 3px 3px"></div>
    <div class="brand"><div class="brand-square" style="width:11px;height:11px"></div><div class="brand-name" style="font-size:24px">TALL PINE</div></div>
    <div class="worker" role="img" aria-label="Worker silhouette pushing up a wall frame" style="width:32px;height:58px;border-radius:12px 12px 3px 3px"></div>
  </div>
  <div class="abs brand-sub" style="left:326px;top:484px;width:160px;font-size:10px">GENERAL CONSTRUCTION INC</div>

  <div class="abs contact" style="left:314px;top:520px">
    <div class="row"><span class="dot blue"><svg viewBox="0 0 10 10"><path d="M2 1l2 2-1 1.2c.6 1.2 1.6 2.2 2.8 2.8L7 6l2 2-1.3 1.3C4.5 9 1 5.5.7 2.3Z" fill="#fff"/></svg></span><span class="phone">508-374-2915</span></div>
    <div class="row"><span class="dot red"><svg viewBox="0 0 10 10"><rect x="1" y="2.5" width="8" height="5.5" fill="none" stroke="#fff" stroke-width="1"/><path d="M1 2.5l4 3 4-3" fill="none" stroke="#fff" stroke-width="1"/></svg></span><span class="email">tpgcsince2004@mailbox.example</span></div>
  </div>

  <div class="abs company-name" style="left:106px;top:394px">
    <span class="w-red">TALL</span><span class="w-boxed">PINE</span>GENERAL<br>CONSTRUCTION INC
  </div>
  <div class="abs tagline" style="left:114px;top:461px">
    <span>I can do all things through Christ</span><br><span>who strengthens me" Philippians 4:13</span>
  </div>
  <ul class="abs services" style="left:94px;top:515px">
    <li><svg viewBox="0 0 12 12"><path d="M1 6L6 1.5 11 6V11H1Z" fill="none" stroke="#fff" stroke-width="1.3"/></svg><span>Remodeling Services</span></li>
    <li><svg viewBox="0 0 12 12"><path d="M1 6L6 1.5 11 6V11H1ZM1 8.5H11M6 4V11" fill="none" stroke="#fff" stroke-width="1.1"/></svg><span>Structural Framing Services</span></li>
    <li><svg viewBox="0 0 12 12"><path d="M2 11L7 6M5 3.5L8.5 1 11 3.5 8.5 6Z" fill="none" stroke="#fff" stroke-width="1.4"/></svg><span>Residential &amp; Commercial Construction</span></li>
  </ul>
  <div class="abs website" style="left:537px;top:560px">tpgcinc.example</div>

  <!-- Front -->
  <div class="abs front-contact" style="left:85px;top:744px;width:330px;text-align:center">508-374-2915 | tpgcsince2004@mailbox.example</div>
  <div class="abs logo-lockup" style="left:174px;top:900px;width:136px;height:30px">
    <div class="worker" role="img" aria-label="Worker silhouette pushing up a wall frame" style="width:18px;height:28px;border-radius:6px 6px 2px 2px"></div>
    <div class="brand"><div class="brand-square" style="width:7px;height:7px"></div><div class="brand-name" style="font-size:15px">TALL PINE</div></div>
    <div class="worker" role="img" aria-label="Worker silhouette pushing up a wall frame" style="width:18px;height:28px;border-radius:6px 6px 2px 2px"></div>
  </div>
  <div class="abs brand-sub" style="left:172px;top:933px;width:140px;font-size:6px">GENERAL CONSTRUCTION INC</div>

  <!-- Rear -->
  <div class="abs logo-lockup" style="left:546px;top:772px;width:230px;height:76px">
    <div class="worker light" role="img" aria-label="Worker silhouette pushing up a wall frame" style="width:46px;height:74px;border-radius:14px 14px 4px 4px"></div>
    <div class="brand"><div class="brand-square" style="width:13px;height:13px"></div><div class="brand-name" style="font-size:28px;color:#fff">TALL PINE</div></div>
    <div class="worker light" role="img" aria-label="Worker silhouette pushing up a wall frame" style="width:46px;height:74px;border-radius:14px 14px 4px 4px"></div>
  </div>
  <div class="abs brand-sub" style="left:560px;top:857px;width:210px;font-size:12px;color:#fff">GENERAL CONSTRUCTION INC</div>

  <div class="abs company-name" style="left:516px;top:912px;font-size:20px">
    <span class="w-red">TALL</span><span class="w-boxed">PINE</span>GENERAL<br>CONSTRUCTION INC
  </div>
  <div class="abs tagline" style="left:524px;top:960px;font-size:8.5px">
    I can do all things through Christ<br>who strengthens me" Philippians 4:13
  </div>
  <div class="abs contact" style="left:666px;top:940px">
    <div class="row"><span class="dot blue" style="width:11px;height:11px"><svg viewBox="0 0 10 10"><path d="M2 1l2 2-1 1.2c.6 1.2 1.6 2.2 2.8 2.8L7 6l2 2-1.3 1.3C4.5 9 1 5.5.7 2.3Z" fill="#fff"/></svg></span><span class="phone" style="font-size:23px;line-height:20px">508-374-2915</span></div>
    <div class="row"><span class="dot red" style="width:11px;height:11px"><svg viewBox="0 0 10 10"><rect x="1" y="2.5" width="8" height="5.5" fill="none" stroke="#fff" stroke-width="1"/><path d="M1 2.5l4 3 4-3" fill="none" stroke="#fff" stroke-width="1"/></svg></span><span class="email" style="font-size:8.5px;line-height:11px;background:#fff;padding:0 2px">tpgcsince2004@mailbox.example</span></div>
  </div>

</div>
</body>
</html>
```